TechNurse Atlantic
TechNurse Atlantic - Computers
Creative Brief
Professional
Derwin Halcott Jr., MCP
Partner
47 Marlow Lane Hamilton HM11, Suite 208 Bermuda
dhalcott@wirelunabda.com
http://www.wirelunabda.com
Please note that #21 is the winning logo for TechNurse. Please design stationary based on this, thanks. http://orders.brandquillhub.com/contests/technurse-atlantic

```html
<!DOCTYPE html>
<html lang="en">
<head>
<meta charset="utf-8">
<title>TechNurse Atlantic – Business Card</title>
<link rel="stylesheet" href="https://fonts.googleapis.com/css2?family=Arimo:wght@400;700&family=Michroma&display=swap">
<style>
  :root {
    --bg: #eeeae6;
    --card: #ffffff;
    --card-shade: #e4e4e6;
    --ink: #3a3a3a;
    --ink-soft: #555555;
    --brand-red: #c8161d;
    --brand-dark: #2b2b2b;
    --rule: #b9b9b9;
    --faint: #d9d9dc;
  }
  * { box-sizing: border-box; margin: 0; padding: 0; }
  html, body { width: 1200px; height: 919px; overflow: hidden; }
  body {
    background: var(--bg);
    font-family: "Arimo", Arial, sans-serif;
    color: var(--ink);
    position: relative;
  }
  .card {
    position: absolute;
    width: 575px;
    height: 360px;
    border-radius: 22px;
    background: radial-gradient(ellipse at 40% 35%, var(--card) 40%, var(--card-shade) 100%);
    box-shadow: 0 6px 18px rgba(0,0,0,0.18);
    overflow: hidden;
  }
  .card--front { left: 410px; top: 220px; width: 450px; z-index: 2; }
  .card--back { left: 435px; top: 450px; z-index: 1; }

  .wordmark {
    position: absolute;
    display: flex;
    align-items: center;
    gap: 8px;
    font-family: "Michroma", sans-serif;
    font-weight: 400;
    color: var(--brand-dark);
    white-space: nowrap;
  }
  .wordmark__dot {
    border-radius: 50%;
    background: var(--brand-red);
    flex: none;
  }
  .card--front .wordmark { left: 26px; top: 150px; font-size: 22px; }
  .card--front .wordmark__dot { width: 14px; height: 14px; }
  .tagline {
    position: absolute;
    left: 26px; top: 186px;
    font-size: 6.5px;
    letter-spacing: 0.6px;
    color: var(--ink-soft);
    font-weight: 700;
  }
  .divider {
    position: absolute;
    left: 218px; top: 28px;
    width: 1px; height: 190px;
    background: var(--rule);
  }
  .contact {
    position: absolute;
    left: 234px; top: 34px;
    font-size: 11.5px;
    line-height: 1.35;
    color: var(--ink);
  }
  .contact__name { color: var(--brand-red); font-weight: 700; font-size: 14px; }
  .contact__name small { color: var(--ink); font-weight: 400; font-size: 10px; }
  .contact__role { margin-bottom: 18px; }
  .contact__address { margin-bottom: 18px; }
  .contact dl { display: grid; grid-template-columns: 38px auto; }

  .swoosh { position: absolute; left: 0; bottom: 0; width: 100%; height: 110px; }
  .web {
    position: absolute;
    right: 22px; bottom: 12px;
    font-size: 10.5px;
    color: #ffffff;
    letter-spacing: 0.3px;
  }

  .card--back .wordmark--faint { left: -10px; top: 60px; font-size: 96px; color: var(--faint); gap: 14px; }
  .card--back .wordmark--faint .wordmark__dot { width: 70px; height: 70px; background: var(--faint); }
  .card--back .wordmark--small { right: 38px; top: 255px; font-size: 18px; }
  .card--back .wordmark--small .wordmark__dot { width: 12px; height: 12px; }
  .web--back {
    position: absolute;
    right: 38px; top: 300px;
    font-size: 11px; font-weight: 700;
    color: var(--brand-red);
  }
</style>
</head>
<body>
  <article class="card card--back" aria-label="Business card, back">
    <div class="wordmark wordmark--faint" aria-hidden="true">TechNurse<span class="wordmark__dot"></span></div>
    <div class="wordmark wordmark--small">TechNurse<span class="wordmark__dot"></span></div>
    <p class="web--back">www.wirelunabda.com</p>
  </article>

  <article class="card card--front" aria-label="Business card, front">
    <div class="wordmark">TechNurse<span class="wordmark__dot"></span></div>
    <p class="tagline">EXPERT HOME AND OFFICE COMPUTER SUPPORT</p>
    <div class="divider"></div>
    <div class="contact">
      <p class="contact__name">Derwin Halcott Jr., <small>MCP</small></p>
      <p class="contact__role">Partner</p>
      <p class="contact__address">47 Marlow Lane<br>Hamilton HM11, Suite 208<br>Bermuda</p>
      <dl>
        <dt>Phone:</dt><dd>(441) 290-7316</dd>
        <dt>Cell:</dt><dd>(441) 538-2159</dd>
        <dt>Email:</dt><dd>dhalcott@wirelunabda.com</dd>
      </dl>
    </div>
    <svg class="swoosh" viewBox="0 0 450 110" preserveAspectRatio="none" aria-hidden="true">
      <path d="M0 48 C120 95 300 80 450 60 L450 70 C300 92 120 104 0 62 Z" fill="#2b2b2b"/>
      <path d="M0 62 C130 108 300 92 450 70 L450 110 L0 110 Z" fill="#c8161d"/>
      <path d="M0 90 C150 112 320 100 450 84 L450 110 L0 110 Z" fill="#9e0f15"/>
    </svg>
    <p class="web">www.wirelunabda.com</p>
  </article>
</body>
</html>
```